Web Design Project

I need designs (PSD only - no programming) for several pages of a new website helping train operators to manage key information about their traindrivers.
The main feature of this website is the management of personnel records (create, edit, search, delete). Another key aspect is the management of user privileges. Since this is a new website we also need a user friendly frontpage, pricing information and how it works sections.
This can be broken down into 9 pages for which we need designs (PSDs).
1. Home
2. Driver record
3. How it works
4. Pricing
5. User administration
6. Help
7. Record list view
8. Login
9. Registration
Navigation (not logged in) are: Home | How it works | Pricing | Customers | About us | Contact
Navigation (logged in) are: Overview | Administration | Manage records | Billing | Help | Contact
Footer: Customer logos | Awards | Terms & Conditions | Privacy
To provide the best support for you to come up with a strong design proposal I will provide DAILY feedback to all participants. We have also created concept mockups (attached) and example pages (below) for each section to give you a clear sense of what we look for.
The core concepts for a successful bid are that the website is EASY to understand, INTUITIVE to navigate, and SIMPLE to use. Most of our users lack technical background and are looking for tool to simplify their work.
The strongest participants (winner and close contenders) will have the opportunity to additional commissioned work on additional sections not included in this brief.
Example Pages (by section)
1. http://www.brovendale.example/site-keepers/
1. http://www.qvt.example/
1. http://www.mondaph.example/
1. http://www.gorvanquest.example/
2. http://www.snapveld.example/profile_edit.gne
3. https://www.tarn.example/how-it-works/
3. http://www.bulkvue.example/learn
4. http://www.pactheron.example/crm/editions-pricing.jsp
4. http://www.brovendale.example/site-keepers/prices
6. https://support.talvora.example/en-gb/
6. http://help.dealmeadow.example/contact_us
8. https://www.careweave.example/uas/login
8. https://www.dealmeadow.example/login
8. http://www.askhollow.example/login/index
For form designs we like Verindo, Bidnook, Snapveld, CareWeave, Chatterly and the concepts presented by Tomas Kerrigan in his classic Layout Craft Shaping the Input Boxes.
For additional guidance see mockups attached!
Target Market(s)
Security, human resources and admin support employees for train operators.
Industry/Entity Type
Learn
Requirements
Should not have
- Home page should not have
Social media icons (chatterly, chirpla, CareWeave, RSS feed)
Contact forms
Read more links
Old trains

```html
<!DOCTYPE html>
<html lang="en">
<head>
<meta charset="utf-8">
<title>RailRoster – Home</title>
<link rel="stylesheet" href="https://fonts.googleapis.com/css2?family=Arimo:wght@400&family=Jost:wght@300;400&family=Source+Sans+3:wght@400&display=swap">
<style>
:root{
  --page:#ffffff;
  --band:#fbfcf7;
  --ink:#1a1a1a;
  --nav-bg:#232323;
  --nav-text:#f2c33a;
  --accent-teal:#1a9cc0;
  --hero-blue:#1b56a3;
  --headline-yellow:#f6d23c;
  --link-blue:#2b5fb3;
  --card-line:#bdbdbd;
  --logo-bg:#ededed;
  --rule:#e4e4e4;
  --arrow:#e6b35a;
}
*{margin:0;padding:0;box-sizing:border-box}
html,body{width:842px;height:1200px;overflow:hidden;background:var(--page)}
body{position:relative;font-family:"Source Sans 3",sans-serif;color:var(--ink)}
.abs{position:absolute}

.utility-links{top:42px;left:508px;display:flex;gap:20px;font-size:14px}
.utility-links span{display:flex;align-items:center;gap:6px}
.utility-links svg{width:10px;height:12px}

.hero{left:30px;top:78px;width:781px;height:339px;
  background:linear-gradient(180deg,#6f6a66 0%,#8b8580 35%,#5d5650 65%,#9aa0a5 100%)}
.main-nav{left:82px;top:90px;width:676px;height:47px;background:var(--nav-bg);border-radius:2px}
.main-nav a{position:absolute;top:0;width:94px;height:47px;text-align:center;line-height:46px;
  font-size:14px;color:var(--nav-text);text-decoration:none}
.main-nav a::after{content:"";position:absolute;left:0;right:0;bottom:0;height:4px;background:#fff}
.main-nav a.current{color:#fff}
.main-nav a.current::after{background:var(--accent-teal)}
.hero-title{left:424px;top:216px;width:283px;height:46px;background:var(--hero-blue);
  color:var(--headline-yellow);font-size:28px;line-height:44px;padding-left:9px}
.hero-bar{left:424px;top:266px;width:334px;height:5px;background:var(--hero-blue)}
.hero-text{left:424px;top:276px;width:340px;color:#fff;font-family:"Arimo",sans-serif;font-size:11px;line-height:16px}

.band{left:30px;width:781px;height:215px;background:var(--band)}
.section-title{left:323px;width:194px;height:42px;background:var(--nav-bg);border-radius:2px;
  color:var(--accent-teal);font-family:"Jost",sans-serif;font-weight:300;font-size:24px;
  text-align:center;line-height:42px;letter-spacing:.5px}
.section-copy{left:30px;width:781px;text-align:center;font-family:"Arimo",sans-serif;font-size:11.6px;line-height:16.8px}
.cta{left:0;width:842px;text-align:center;font-family:"Jost",sans-serif;font-size:14px;letter-spacing:.3px}

.carousel-arrow{top:955px;width:20px;height:40px}
.customer-card{top:915px;width:117px;height:119px;border:1px solid var(--card-line);background:#fff}
.customer-card .mark{position:absolute;left:14px;top:22px;width:90px;height:55px;background:var(--logo-bg);
  display:flex;align-items:center;justify-content:center;gap:5px;font-size:11px;color:#333;text-align:center}
.customer-card .mark i{display:block;width:10px;height:10px;background:#555}
.customer-card .label{position:absolute;left:0;right:0;top:86px;text-align:center;font-family:"Arimo",sans-serif;font-size:12px;color:var(--link-blue)}

.footer-rule{left:56px;top:1054px;width:728px;height:1px;background:var(--rule)}
.footer-nav{left:0;top:1087px;width:842px;text-align:center;font-size:14px;word-spacing:0}
.footer-nav span{margin:0 5px}
.copyright{left:0;top:1168px;width:842px;text-align:center;font-family:"Arimo",sans-serif;font-size:11px}
</style>
</head>
<body>

<nav class="abs utility-links">
  <span>Signup <svg viewBox="0 0 10 12"><path d="M0 0L10 6L0 12Z" fill="#f4cf3a"/></svg></span>
  <span>Login <svg viewBox="0 0 10 12"><path d="M0 0L10 6L0 12Z" fill="#f4cf3a"/></svg></span>
  <span>Language <svg viewBox="0 0 10 12"><path d="M0 0L10 6L0 12Z" fill="#f4cf3a"/></svg></span>
</nav>

<div class="abs hero" role="img" aria-label="Photograph of a busy city street lined with tall buildings and shops"></div>

<nav class="abs main-nav">
  <a class="current" style="left:10px">Home</a>
  <a style="left:122px">How It works</a>
  <a style="left:235px">Prices</a>
  <a style="left:347px">Our Customers</a>
  <a style="left:460px">About Us</a>
  <a style="left:572px">Contact</a>
</nav>

<h1 class="abs hero-title">Lorem ipsum dolor sit</h1>
<div class="abs hero-bar"></div>
<p class="abs hero-text">Lorem ipsum dolor sit amet, consectetur adipiscing elit. Proin aliquam<br>laoreet mi</p>

<section>
  <div class="abs band" style="top:430px"></div>
  <h2 class="abs section-title" style="top:434px">BENIFITS</h2>
  <p class="abs section-copy" style="top:489px">Lorem ipsum dolor sit amet, consectetur adipiscing elit. Proin aliquam laoreet mi, quis pellentesque sem tincidunt sit amet. Praesent rutrum<br>tincidunt nequ e sed volutpat. Sed pulvinar pre tium tincidunt. Etiam et risus sit amet nulla consectetur aliquam. Suspendisse vitae ipsum turpis.<br>Vivamus massa ligula, tempus id euismod nec, molestie eget elit. Maecenas iaculis auctor ju&nbsp; sto. Curabitur pretium enim in leo congue vestibulum.<br>Praesent volutpat ultrices eros convallis&nbsp; dapibus. Duis erat lectus, fringill id blandit quis, condimentum non leo. Nunc ipsum arcu, accumsan sed<br>pulvinar non, pharetra vel orci. Nam posuere aliquam mattis. Aenean felis nisl, tempus in dignissim sit amet, fermentum id tortor. Curabitur<br>hendrerit metus sit amet metus aliquam&nbsp; commodo. Vivamus eget risus ur na, vitae dictum dolor.</p>
  <p class="abs cta" style="top:611px">SIGN UP OR REQUEST A CALL</p>
</section>

<section>
  <div class="abs band" style="top:663px"></div>
  <h2 class="abs section-title" style="top:673px">HOW IT WORKS</h2>
  <p class="abs section-copy" style="top:728px">Lorem ipsum dolor sit amet, consectetur adipiscing elit. Proin aliquam laoreet mi, quis pellentesque sem tincidunt sit amet. Praesent rutrum<br>tincidunt nequ e sed volutpat. Sed pulvinar pre tium tincidunt. Etiam et risus sit amet nulla consectetur aliquam. Suspendisse vitae ipsum turpis.<br>Vivamus massa ligula, tempus id euismod nec, molestie eget elit. Maecenas iaculis auctor ju&nbsp; sto. Curabitur pretium enim in leo congue vestibulum.<br>Praesent volutpat ultrices eros convallis&nbsp; dapibus. Duis erat lectus, fringill id blandit quis, condimentum non leo. Nunc ipsum arcu, accumsan sed<br>pulvinar non, pharetra vel orci. Nam posuere aliquam mattis. Aenean felis nisl, tempus in dignissim sit amet, fermentum id tortor. Curabitur<br>hendrerit metus sit amet metus aliquam&nbsp; commodo. Vivamus eget risus ur na, vitae dictum dolor.</p>
  <p class="abs cta" style="top:850px">SIGN UP OR REQUEST A CALL</p>
</section>

<section class="customers">
  <svg class="abs carousel-arrow" style="left:33px" viewBox="0 0 20 40"><path d="M20 0.5A19.5 19.5 0 0 0 20 39.5" fill="#fff" stroke="#bbb"/><path d="M13 14L6 20L13 26Z" fill="none" stroke="var(--arrow)" stroke-width="1.2"/></svg>
  <svg class="abs carousel-arrow" style="left:787px" viewBox="0 0 20 40"><path d="M0 0.5A19.5 19.5 0 0 1 0 39.5" fill="#fff" stroke="#bbb"/><path d="M7 14L14 20L7 26Z" fill="none" stroke="#bbb" stroke-width="1.2"/></svg>

  <div class="abs customer-card" style="left:56px"><div class="mark"><i></i>Harrow's Picks</div><div class="label">Lorem</div></div>
  <div class="abs customer-card" style="left:178px"><div class="mark">LawnStead</div><div class="label">Lorem</div></div>
  <div class="abs customer-card" style="left:300px"><div class="mark">GreenOrb</div><div class="label">Lorem</div></div>
  <div class="abs customer-card" style="left:423px"><div class="mark"><i></i>Kestrin</div><div class="label">Lorem</div></div>
  <div class="abs customer-card" style="left:545px"><div class="mark">Ridge Meadow</div><div class="label">Lorem</div></div>
  <div class="abs customer-card" style="left:667px"><div class="mark">Olden &amp; Pryce</div><div class="label">Lorem</div></div>
</section>

<div class="abs footer-rule"></div>
<footer>
  <nav class="abs footer-nav">Home<span>|</span> How it Works <span>|</span> Prices <span>|</span> Our Customers <span>|</span> About Us <span>|</span> Contact <span>|</span> Career <span>|</span> Sitemap <span>|</span></nav>
  <p class="abs copyright">Copywrite © 2012 RailRoster | All rights reserved | T&amp;C</p>
</footer>

</body>
</html>
```